Packaging design - PROTEIN BALLS

PACKAGING
The packaging is a round carton roll, size: Ø73x180 mm, mockup sample enclosed, The label on the carton roll should have a size of 225x178 mm (width x height)

PRODUCT
Chrunchy, cheesy PROTEIN BALLS (100% pure cheese) with a huge amount of protein (65%), a lot of calcium and very low carbogydrates (3%). Diameter about 1.5 cm.

DESIGN
Since our customers are very sporty people, runner, bodybuilder, etc. The design must fit to this sporty customer segment.

FILES
We need the open data for InDesign with all fonts and pictures. If there are licenses tu buy, we will do it.

SUMMARY
1. SNACK
• Crunchy cheese balls with a diameter of about 1.5cm
• 3 different flavors: "Swiss Alpine Salt", "Provencale" and "Hot Chili"
• High in Protein (65%) and Calcium (2%)
• Low in carbohydrates (3%)

2. PACKAGING
• Carton roll, size: Ø73x180 mm
• Background can be every color, but we think a black one will be high premium.
• Maybe different sports are represented in the background, maybe also cheese
• Be creative
• Label applied, size: 225x178 mm

3. DESIGN
• Product name = (Cheese) PROTEIN BALLS
• 3 different colors for the 3 flavors "Swiss Alpine Salt", "Provencale" and "Hot Chili"
• HighProtein, High Calcium and LowCarb must be pointed out on the front
• Swissness: Swiss made must be pointed out
• fresh and young design, most customers are sporty people, pumper with a strong body awareness

TARGET CUSTOMER
Our main customers are extremely sporty people, who work very hard on their muscles and fitness, most of them are runners, cross fitnesser, bodybuilders, etc We will launch the product in fitness centers, in supplement shops and we are planning to make some stories with sporty influencer.

Serif
Sans Serif

• Cheese, naturalness, healthy, PROTEIN balls, muscles, Swissness must showed on the product.

```html
<!DOCTYPE html>
<html lang="en">
<head>
<meta charset="utf-8">
<title>Protein Balls – Swiss Alpine Salt label</title>
<link href="https://fonts.googleapis.com/css2?family=Alfa+Slab+One&family=Arimo:wght@400;700&family=Josefin+Sans:wght@400;600&family=Kaushan+Script&family=Oswald:wght@300;500&family=Pacifico&display=swap" rel="stylesheet">
<style>
  :root {
    --ink: #000000;
    --paper: #ffffff;
    --sky: #8ab8e6;
    --sky-muted: #6f98c2;
    --swiss-red: #e0202a;
    --photo-cream: #d9d39a;
    --illus-yellow: #f2c230;
    --placeholder-grey: #a6a6a6;
  }
  * { box-sizing: border-box; margin: 0; padding: 0; }
  html, body { width: 1200px; height: 883px; overflow: hidden; background: var(--paper); }
  .label {
    position: absolute; left: 67px; top: 20px; width: 1066px; height: 842px;
    background: var(--ink); color: var(--paper); overflow: hidden;
  }
  .label > * { position: absolute; }
  .base-band { left: 0; bottom: 0; width: 100%; height: 26px; background: var(--sky); }
  .divider { height: 10px; background: var(--sky-muted); }
  /* swiss ribbon */
  .swiss-ribbon { left: 586px; top: 0; width: 76px; height: 113px; }
  .made-in {
    left: 664px; top: 13px; writing-mode: vertical-rl;
    font: 400 12px/1 "Arimo", sans-serif;
  }
  /* about column */
  .about-title { left: 56px; top: 50px; font: 400 34px/1 "Pacifico", cursive; }
  .about-text {
    left: 68px; top: 101px; width: 232px;
    font: 400 17px/20px "Josefin Sans", sans-serif; letter-spacing: 0.3px;
  }
  .tagline {
    left: 48px; top: 436px; width: 264px; text-align: center;
    font: 400 26px/1.2 "Kaushan Script", cursive;
  }
  .snack-illustration {
    left: 132px; top: 493px; width: 96px; height: 64px; border-radius: 8px;
    background: linear-gradient(90deg, var(--sky) 0 40%, var(--illus-yellow) 40%);
  }
  .claim-badge {
    top: 649px; width: 46px; height: 84px; border: 2px solid var(--paper);
    border-radius: 8px 8px 0 0; overflow: hidden; display: flex; flex-direction: column;
  }
  .claim-badge .claim-name {
    flex: 1; display: flex; align-items: center; justify-content: center; text-align: center;
    font: 500 8.5px/1.15 "Oswald", sans-serif; text-transform: uppercase;
  }
  .claim-badge .claim-value {
    height: 38px; background: var(--sky); display: flex; align-items: center; justify-content: center;
    font: 500 19px/1 "Oswald", sans-serif;
  }
  .net-weight { left: 76px; top: 782px; width: 200px; text-align: center; font: 600 15px/1 "Josefin Sans", sans-serif; }
  /* front panel */
  .front { left: 398px; top: 0; width: 272px; height: 842px; text-align: center; }
  .front > * { position: absolute; left: 0; width: 100%; }
  .brand-name {
    top: 92px; left: 14px !important; width: auto !important;
    font: 400 58px/1 "Pacifico", cursive; color: var(--sky);
  }
  .cheese-seal {
    top: 117px; left: 188px !important; width: 64px !important; height: 64px;
    border: 2px solid var(--paper); border-radius: 50%;
  }
  .slab { font-family: "Alfa Slab One", serif; font-weight: 400; line-height: 1; white-space: nowrap; }
  .product-line1 { top: 173px; font-size: 50px; }
  .product-line2 { top: 224px; font-size: 58px; }
  .flavour {
    top: 293px; left: 6px !important; width: 264px !important; height: 52px; background: var(--sky);
    border-radius: 4px; font: 500 29px/52px "Oswald", sans-serif; text-transform: uppercase; letter-spacing: -0.5px;
  }
  .product-photo {
    top: 377px; left: 36px !important; width: 198px !important; height: 92px; border-radius: 46px;
    background: radial-gradient(ellipse at center, #e6e0ae, var(--photo-cream) 60%, #b8b070);
  }
  .front .divider { left: 4px; width: 264px; }
  .claim-high { top: 507px; font-size: 80px; }
  .claim-protein { top: 587px; font-size: 44px; }
  .claim-amp { top: 621px; font-size: 32px; z-index: 1; }
  .claim-calcium { top: 651px; font-size: 44px; }
  .claim-rule { top: 713px; left: 46px !important; width: 180px !important; height: 2px; background: var(--paper); }
  .claim-lowcarb { top: 727px; font-size: 37px; }
  /* nutrition */
  .nutrition {
    left: 779px; top: 57px; width: 222px; height: 381px; background: var(--paper); color: var(--ink);
    padding: 5px 9px; font: 400 9.5px/1 "Arimo", sans-serif;
  }
  .nutrition h2 { font: 700 24px/1 "Arimo", sans-serif; margin-bottom: 3px; }
  .nf-row { display: flex; justify-content: space-between; padding: 2px 0; border-bottom: 1px solid #999; }
  .nf-row.plain { border: 0; padding: 0; }
  .nf-row.sub { padding-left: 17px; }
  .nf-bar { height: 6px; background: var(--ink); margin: 2px 0; }
  .nf-dv { text-align: right; font-size: 6px; font-weight: 700; padding: 2px 0; border-bottom: 1px solid #999; }
  .nutrition b { font-weight: 700; }
  .nf-note { font-size: 6.5px; line-height: 1.4; padding-top: 3px; border-bottom: 3px solid var(--ink); padding-bottom: 2px; }
  /* producer */
  .mini-brand { left: 778px; top: 463px; width: 140px; text-align: left; }
  .mini-brand .brand-small { font: 400 24px/1.1 "Pacifico", cursive; color: var(--sky); margin-left: 14px; }
  .mini-brand .slab { font-size: 23px; }
  .mini-brand .balls-small { font-size: 25px; margin-left: 12px; }
  .producer { left: 779px; top: 575px; font: 400 16px/20px "Josefin Sans", sans-serif; letter-spacing: 0.6px; font-style: normal; }
  .producer .producer-label { color: var(--sky); font-weight: 600; text-transform: uppercase; }
  .barcode-box {
    left: 778px; top: 717px; width: 206px; height: 78px; background: var(--paper);
    color: var(--placeholder-grey); font: 300 17px/1 "Oswald", sans-serif; padding: 23px 0 0 13px;
  }
</style>
</head>
<body>
<main class="label">
  <section class="about-title">About</section>
  <p class="about-text">Lorem ipsum dolor sit amet, consectetur adip-iscing elit. Nulla varius et ligula quis sagittis. Praesent aliquam metus ipsum, non sodales ipsum faucibus eu. Ut ac rutrum elit. Proin rutrum dictum varius. Vestibulum at rutrum turpis, ac sodales magna. Nunc varius leo massa, ac fermentum est volutpat ac.</p>
  <div class="divider" role="img" aria-label="Blue diagonal stripe divider" style="left:48px;top:407px;width:264px"></div>
  <p class="tagline">Cheezy crunchy snack</p>
  <div class="snack-illustration" role="img" aria-label="Illustration of a salt shaker beside a wedge of cheese"></div>
  <div class="divider" role="img" aria-label="Blue diagonal stripe divider" style="left:48px;top:580px;width:264px"></div>

  <div class="claim-badge" style="left:86px"><span class="claim-name">High<br>Protein</span><span class="claim-value">65%</span></div>
  <div class="claim-badge" style="left:158px"><span class="claim-name">High<br>Calcium</span><span class="claim-value">2%</span></div>
  <div class="claim-badge" style="left:228px"><span class="claim-name">Low<br>Carbo-<br>hydrates</span><span class="claim-value">65%</span></div>
  <p class="net-weight">Net WT: 300g</p>

  <svg class="swiss-ribbon" viewBox="0 0 76 113" aria-label="Swiss flag ribbon">
    <polygon points="0,0 76,0 76,113 38,98 0,113" fill="var(--swiss-red)"/>
    <rect x="32" y="24" width="12" height="42" fill="var(--paper)"/>
    <rect x="17" y="39" width="42" height="12" fill="var(--paper)"/>
  </svg>
  <p class="made-in">Made in Switzerland</p>

  <section class="front">
    <p class="brand-name">Kasli</p>
    <div class="cheese-seal"></div>
    <h1 class="slab product-line1">PROTEIN</h1>
    <p class="slab product-line2">BALLS</p>
    <p class="flavour">Swiss Alpine Salt</p>
    <div class="product-photo" role="img" aria-label="Photo of three cheese protein balls"></div>
    <div class="divider" role="img" aria-label="Blue diagonal stripe divider" style="top:497px"></div>
    <p class="slab claim-high">HIGH</p>
    <p class="slab claim-protein">PROTEIN</p>
    <p class="slab claim-amp">&amp;</p>
    <p class="slab claim-calcium">CALCIUM</p>
    <div class="claim-rule"></div>
    <p class="slab claim-lowcarb">LOW CARB</p>
    <div class="divider" role="img" aria-label="Blue diagonal stripe divider" style="top:781px"></div>
  </section>

  <section class="nutrition">
    <h2>Nutrition Facts</h2>
    <div class="nf-row plain"><span>Serving Size</span><span>...g</span></div>
    <div class="nf-row plain"><span>Servings Per Container</span></div>
    <div class="nf-bar"></div>
    <div class="nf-row"><b>Amount Per Serving</b></div>
    <div class="nf-row"><span><b>Calories</b> ....</span><span>Calories from Fat ...</span></div>
    <div class="nf-dv">% Daily Value*</div>
    <div class="nf-row"><span><b>Total Fat</b> ...g</span><b>...%</b></div>
    <div class="nf-row sub"><span>Saturated Fat ...g</span><b>...%</b></div>
    <div class="nf-row sub"><span><i>Trans</i> Fat ...g</span></div>
    <div class="nf-row"><span><b>Cholestrol</b> ...mg</span><b>...%</b></div>
    <div class="nf-row"><span><b>Sodium</b> ...mg</span><b>...%</b></div>
    <div class="nf-row"><span><b>Total Carbohydrate</b> ...g</span><b>...%</b></div>
    <div class="nf-row sub"><span>Dietary Fiber ...g</span><b>...%</b></div>
    <div class="nf-row sub"><span>Sugars ...g</span></div>
    <div class="nf-row plain" style="padding:2px 0"><span><b>Protein</b> ...g</span></div>
    <div class="nf-bar"></div>
    <div class="nf-row"><span>Vitamin A</span><b>...%</b></div>
    <div class="nf-row"><span>Vitamin C</span><b>...%</b></div>
    <div class="nf-row"><span>Calcium</span><b>...%</b></div>
    <div class="nf-row"><span>Iron</span><b>...%</b></div>
    <p class="nf-note">*Percent Daily Values are based on a 2,000 calorie diet. Your Daily Values may be higer or lower depending on your calorie needs.</p>
  </section>

  <div class="mini-brand">
    <p class="brand-small">Kasli</p>
    <p class="slab">PROTEIN</p>
    <p class="slab balls-small">BALLS</p>
  </div>
  <address class="producer">
    <span class="producer-label">Produced by</span><br>
    Company<br>Address<br>Phone<br>www.company.com
  </address>
  <div class="barcode-box">BARCODE</div>

  <div class="base-band"></div>
</main>
</body>
</html>
```